TAVORA MED -DIAGNOSTIC CENTRE FOR IMAGES

Our Activity provides diagnostic services for images (RMI, Tac, RX, Ultrasound etc.)
We would like to create a broschure that illustrates our services.
We would like to give maximum attention to the Diagnostic service dedicated to "HEART", therefore maximum evidence to the world of Cardiology.
In the background we would like to highlight the other diagnostic services dedicated to the Rest of the Body (Brain, Knees Legs etc.)
Target Market(s)
PERSONS WHO NEED TO PERFORM DIAGNOSTIC TESTS (MRI, CT, ULTRASOUND, RX ETC.)
Industry/Entity Type
HEALTH
Requirements
Must have
- The company logo, must have diagnostic images (MRI, CT, X-ray, ultrasound), must be simple and intuitive, which is harmonious with the colors of our company logo
Should not have
- Colours that are not in harmony with our company logo

```html
<!DOCTYPE html>
<html lang="en">
<head>
<meta charset="utf-8">
<title>Tavora Med – Diagnostic Brochure</title>
<link rel="stylesheet" href="https://fonts.googleapis.com/css2?family=Montserrat:wght@400;500;600;700;800&display=swap">
<style>
  :root{
    --bg:#dcedf7;
    --page:#eef6fb;
    --ink:#16181c;
    --blue:#1d6fc0;
    --blue-dark:#1558a6;
    --teal:#15a3a0;
    --photo-a:#c9e1f1;
    --photo-b:#8fc3e6;
    --text:#3a4350;
  }
  *{margin:0;padding:0;box-sizing:border-box}
  html,body{width:1200px;height:675px;overflow:hidden}
  body{background:var(--bg);font-family:"Montserrat",sans-serif;color:var(--ink);position:relative}
  .page{position:absolute;background:linear-gradient(180deg,#f4f9fd 0%,var(--page) 100%);overflow:hidden;box-shadow:0 8px 24px rgba(30,80,120,.18)}
  .page--front{left:207px;top:71px;width:378px;height:534px}
  .page--back{left:614px;top:68px;width:381px;height:538px}
  .abs{position:absolute}
  .brand{font-weight:700;color:var(--teal);font-size:15px;letter-spacing:.5px;display:flex;align-items:center;gap:5px}
  .brand-dot{width:8px;height:8px;border-radius:50%;background:var(--teal)}
  .headline{left:28px;top:62px;font-weight:700;font-size:19px;line-height:23px}
  .headline span{display:block;color:var(--blue)}
  .intro{left:29px;width:265px;font-size:7.4px;line-height:10.8px;color:var(--text)}
  .photo-hero{left:0;top:170px}
  .call-badge{left:24px;top:482px;width:145px;height:22px;background:var(--blue-dark);color:#fff;font-weight:700;font-size:12px;display:flex;align-items:center;justify-content:center;border-radius:2px}
  .web{left:29px;top:513px;color:#fff;font-size:9.5px;font-weight:500}
  .services-title{right:19px;top:24px;font-size:20px;font-weight:800}
  .services-title span{color:var(--blue)}
  .svc{font-size:8.3px;font-weight:700;color:var(--blue);line-height:9.5px}
  .svc::before{content:"✓";position:absolute;left:-11px;top:0;font-size:8px}
  .svc ul{list-style:none;margin-top:3px;font-weight:500;color:var(--text);font-size:5.4px;line-height:8.3px}
  .lead{font-size:11px;font-weight:700;line-height:13px}
  .lead-text{font-size:7.4px;line-height:10.5px;color:var(--text);margin-top:5px}
  .contact{left:21px;width:184px;height:24px;background:linear-gradient(90deg,var(--teal),var(--blue));color:#fff;font-size:6.5px;font-weight:700;display:flex;align-items:center;gap:8px;padding-left:8px;border-radius:2px}
  .contact small{display:block;font-weight:500;font-size:6.5px}
</style>
</head>
<body>

<section class="page page--front">
  <svg class="abs" style="left:0;top:0" width="80" height="50" aria-hidden="true">
    <rect x="0" y="25" width="48" height="22" fill="#cfe4f2"/>
    <rect x="26" y="0" width="22" height="22" fill="#d8eaf5"/>
    <rect x="50" y="23" width="25" height="24" fill="#dbecf6"/>
  </svg>
  <div class="brand abs" style="right:20px;top:22px"><span class="brand-dot"></span>TAVORA MED</div>

  <h1 class="headline abs">Leading the Way in<span>Healthcare Diagnostics</span></h1>
  <p class="intro abs" style="top:117px">Elevate your well-being with our exceptional healthcare diagnostics. As leaders in the field, we empower you with accurate and insightful information about your health.</p>
  <p class="intro abs" style="top:155px">At our diagnostic center, we understand that your heart's well-being is paramount to your overall health. Our team of skilled cardiologists and medical professionals is committed to guiding you through every step of your diagnostic journey.</p>

  <svg class="abs photo-hero" width="378" height="364" viewBox="0 0 378 364">
    <defs>
      <linearGradient id="heroFill" x1="0" y1="0" x2="1" y2="1">
        <stop offset="0" stop-color="var(--photo-a)"/>
        <stop offset="1" stop-color="var(--photo-b)"/>
      </linearGradient>
      <linearGradient id="floorFill" x1="0" y1="0" x2="1" y2="0">
        <stop offset="0" stop-color="#5db4e6"/>
        <stop offset="1" stop-color="#2a8ad4"/>
      </linearGradient>
    </defs>
    <polygon points="0,180 378,30 378,364 0,364" fill="url(#heroFill)" role="img" aria-label="Smiling cardiologist in white coat holding a clipboard beside a scanner"/>
    <polygon points="190,215 378,65 378,80 198,222" fill="var(--teal)"/>
    <polygon points="0,300 230,290 230,364 0,364" fill="url(#floorFill)"/>
    <polygon points="230,364 378,250 378,364" fill="var(--blue-dark)"/>
    <rect x="325" y="297" width="18" height="18" fill="#3d8fd6"/>
    <rect x="345" y="318" width="18" height="18" fill="#2a7cc8"/>
    <line x1="90" y1="165" x2="75" y2="195" stroke="var(--blue)" stroke-width="3"/>
    <line x1="95" y1="230" x2="110" y2="245" stroke="var(--blue)" stroke-width="3"/>
    <circle cx="105" cy="105" r="60" fill="#c7b9a8" stroke="var(--blue)" stroke-width="3" role="img" aria-label="Doctor reviewing results with a patient seated by an MRI scanner"/>
    <circle cx="64" cy="209" r="39" fill="#d9cfc4" stroke="var(--blue)" stroke-width="3" role="img" aria-label="Physician consulting a patient in a clinic room"/>
    <circle cx="131" cy="264" r="33" fill="#9fb6c9" stroke="var(--blue)" stroke-width="3" role="img" aria-label="Specialist examining a chest X-ray"/>
  </svg>

  <div class="call-badge abs">CALL US 640-318-274</div>
  <div class="web abs">www.tavoramed.com</div>
</section>

<section class="page page--back">
  <svg class="abs" style="left:0;top:0" width="160" height="90" aria-hidden="true">
    <polygon points="0,0 148,0 0,85" fill="var(--blue)"/>
    <rect x="17" y="0" width="16" height="16" fill="#3d8fd6"/>
    <rect x="35" y="18" width="16" height="16" fill="#3d8fd6"/>
    <rect x="15" y="37" width="16" height="16" fill="#2a7cc8"/>
  </svg>
  <h2 class="services-title abs">OUR <span>SERVICES</span></h2>

  <div class="svc abs" style="left:180px;top:72px">Cardiac Diagnostics<ul><li>ECG (Electrocardiogram)</li><li>Stress Test</li><li>Echocardiogram</li></ul></div>
  <div class="svc abs" style="left:180px;top:119px">Gastrointestinal<br>Diagnostics<ul><li>Endoscopy</li><li>Upper GI Series</li></ul></div>
  <div class="svc abs" style="left:180px;top:164px">Advanced Imaging<ul><li>X-ray</li><li>Ultrasound</li><li>MRI</li></ul></div>
  <div class="svc abs" style="left:285px;top:73px">Respiratory Tests<ul><li>Pulmonary Function Test</li><li>Spirometry</li></ul></div>
  <div class="svc abs" style="left:285px;top:107px">Laboratory Tests<ul><li>Urinalysis</li><li>DNA Testing</li><li>Blood Tests</li></ul></div>
  <div class="svc abs" style="left:285px;top:152px">Neurological Tests<ul><li>EEG (Electroencephalogram)</li><li>EMG (Electromyography)</li></ul></div>

  <div class="abs" role="img" aria-label="Digital X-ray system with table and wall detector" style="left:17px;top:101px;width:160px;height:181px;background:linear-gradient(160deg,#f1f5f8,#d6e1ea);border-radius:4px"></div>

  <div class="abs" style="left:198px;top:228px;width:160px">
    <p class="lead">Your well-being journey commences with us.</p>
    <p class="lead-text">Trailblazers in healthcare diagnostics, we provide a roadmap to better health.</p>
  </div>

  <div class="abs" style="left:21px;top:314px;width:160px">
    <p class="lead">Schedule an Appointment with us!</p>
    <p class="lead-text">Reach out to us today and take the first step towards a healthier you. Our dedicated team is here to assist you.</p>
  </div>

  <div class="abs" role="img" aria-label="Ultrasound scanner cart with monitor and scan image" style="left:195px;top:314px;width:170px;height:210px;background:linear-gradient(180deg,#2c3a4a 0%,#52606d 40%,#e3e8ec 60%,#cfd6dc 100%);border-radius:4px"></div>

  <div class="contact abs" style="top:376px">
    <svg width="9" height="9" viewBox="0 0 24 24" aria-hidden="true"><path fill="#fff" d="M6.6 10.8a15 15 0 0 0 6.6 6.6l2.2-2.2c.3-.3.7-.4 1-.2 1.1.4 2.3.6 3.6.6.6 0 1 .4 1 1V20c0 .6-.4 1-1 1A17 17 0 0 1 3 4c0-.6.4-1 1-1h3.5c.6 0 1 .4 1 1 0 1.3.2 2.5.6 3.6.1.3 0 .7-.2 1z"/></svg>
    <span>CALL US <span style="font-weight:500">640-318-274</span></span>
  </div>
  <div class="contact abs" style="top:405px">
    <svg width="9" height="9" viewBox="0 0 24 24" aria-hidden="true"><path fill="#fff" d="M3 5h18v14H3zm2 2v.5l7 4.5 7-4.5V7z"/></svg>
    <span>EMAIL US<small>CONTACT@TAVORAMED.COM</small></span>
  </div>
  <div class="contact abs" style="top:434px">
    <svg width="9" height="9" viewBox="0 0 24 24" aria-hidden="true"><circle cx="12" cy="12" r="9" fill="none" stroke="#fff" stroke-width="2"/><path d="M3 12h18M12 3c3 3 3 15 0 18M12 3c-3 3-3 15 0 18" fill="none" stroke="#fff" stroke-width="1.6"/></svg>
    <span>VISIT OUR WEBSITE<small>WWW.TAVORAMED.COM</small></span>
  </div>

  <div class="brand abs" style="left:21px;top:498px"><span class="brand-dot"></span>TAVORA MED</div>
</section>

</body>
</html>
```